Promotional Flyer/Email Design - Cabling services for Broadcast and Audio Visual

We need a promotional flyer/email design to help launch our company, Velcor Lane. We provide cabling services for Broadcast Television and Audio Visual systems. Recent projects include major television events such as the Harrowmere Racquet Classic and Audio Visual/Entertainment systems for wealthy clients in their homes and on-board super yachts.

The flyer will be printed as single sided A5 and also be sent out in the body of a promotional email. It should feature the company logo along with a complementary colour scheme. It should have a clean finish with images that show the type of work we do (cabling and equipment installation) or the setting for these systems (tv studio, super yacht, cinema room, meeting room with projector etc.)

Services we offer are:

Broadcast/AV system design
On-site installation
Rack building
Pre-fabricated cable looms
Fibre optic installation

About the company:

Velcor Lane provide cabling services for Broadcast Television and Audio Visual systems. With over 15 years experience working in these industries we can help with every aspect of design, project managment, installation and maintenance. Our projects range from fibre optic cabling at major sports events to installing and commisioning bespoke control systems on some of the worlds largest super yachts.

Contact details:

To get a quote or discuss your project contact us now
Telephone: TBC
Email: info@velcor-lane.com
Website: www.velcor-lane.com
Address: TBC

Other information:

The company is based in London, UK. Our projects often take place in other countries with work taking place accross Europe and beyond.

We have a London based workshop for rack building and cable pre-fabrication.

Our website is www.velcor-lane.com

Images:

Images attached can be editted for use on the flyer or have ideas taken from them. Only the company logo is required to feature on the final design.

Target Market(s)

Business to business

Industry/Entity Type

It Company

Font styles to use
Sans Serif

Requirements
Must have
• Company logo
• List of services
• Contact details
Nice to have
• Image of cabling, home cinema room, super yacht, luxury home, outside broadcast truck, fibre optic equipment or cabling.

```html
<!DOCTYPE html>
<html lang="en">
<head>
<meta charset="utf-8">
<title>Velcor Lane – Broadcast &amp; AV Cabling</title>
<link href="https://fonts.googleapis.com/css2?family=Raleway:wght@400;500;600;700&display=swap" rel="stylesheet">
<style>
  :root {
    --crimson: #b5273f;
    --slate-blue: #5670a8;
    --ink: #1e1e1e;
    --brand-grey: #3b3b3d;
    --paper: #ffffff;
    --cable-tone-a: #8a8f92;
    --cable-tone-b: #c9cdd0;
    --rack-tone-a: #3a3d42;
    --rack-tone-b: #a9adb0;
    --room-tone-a: #d9cfc2;
    --room-tone-b: #8f8679;
  }
  * { box-sizing: border-box; margin: 0; padding: 0; }
  html, body { width: 846px; height: 1200px; overflow: hidden; background: var(--paper); }
  body { font-family: "Raleway", sans-serif; color: var(--ink); }

  .flyer { position: relative; width: 846px; height: 1200px; overflow: hidden; background: var(--paper); }

  .backdrop { position: absolute; inset: 0; width: 846px; height: 1200px; }

  .brand {
    position: absolute; left: 80px; top: 140px;
    display: flex; align-items: center; gap: 12px;
  }
  .brand-square { width: 30px; height: 30px; background: var(--slate-blue); }
  .brand-name { font-weight: 600; font-size: 38px; color: var(--brand-grey); letter-spacing: -0.5px; }

  .contact {
    position: absolute; left: 407px; top: 64px; width: 400px;
    text-align: center; font-size: 22px; line-height: 28.8px;
  }
  .contact-lead { font-weight: 700; font-size: 22.5px; }

  .about {
    position: absolute; left: 20px; top: 284px; width: 806px;
    text-align: center; font-size: 19.6px; line-height: 26.6px; font-weight: 400;
  }

  .services {
    position: absolute; left: 223px; top: 560px; width: 400px;
    text-align: center; font-size: 22.5px; line-height: 29px;
  }
  .services-title { font-weight: 700; font-size: 21.5px; }
  .services-list { list-style: none; }

  .gallery { position: absolute; left: 0; top: 789px; width: 846px; height: 310px; }
  .photo { position: absolute; top: 0; height: 310px; }
  .photo-cabling { left: 0; width: 222px; background: linear-gradient(160deg, var(--cable-tone-b), var(--cable-tone-a)); }
  .photo-rack { left: 224px; width: 225px; background: linear-gradient(90deg, var(--rack-tone-b) 0%, var(--rack-tone-a) 55%, var(--rack-tone-b) 100%); }
  .photo-room { left: 451px; width: 395px; background: linear-gradient(150deg, var(--room-tone-a), var(--room-tone-b)); }

  .foreground { position: absolute; left: 0; top: 0; width: 846px; height: 1200px; pointer-events: none; }

  .web-address {
    position: absolute; left: 0; top: 1130px; width: 846px;
    text-align: center; color: var(--paper); font-size: 32px; font-weight: 600;
  }
  .web-address b { font-weight: 700; }
</style>
</head>
<body>
<main class="flyer">
  <svg class="backdrop" viewBox="0 0 846 1200" aria-hidden="true">
    <rect width="846" height="1200" fill="var(--paper)"/>
    <path d="M0 0 H846 V44 H330 C180 44 60 120 0 262 Z" fill="var(--crimson)"/>
  </svg>

  <div class="brand">
    <span class="brand-square"></span>
    <span class="brand-name">Velcor Lane</span>
  </div>

  <address class="contact" style="font-style:normal">
    <p class="contact-lead">To get a quote or discuss your<br>project contact us now</p>
    <p>Telephone: TBC</p>
    <p>Email: info@velcor-lane.com</p>
    <p>Website: www.velcor-lane.com</p>
    <p>Address: TBC</p>
  </address>

  <section class="about">
    <p>Velcor Lane provides cabling services for Broadcast Television and Audio Visual systems. With over 15 years experience working in these industries, we can help with every aspect of design, project management, installation and maintenance. Our projects range from fibre optic cabling at major sports events to installing and commissioning bespoke control systems on some of the worlds largest super yachts.</p>
    <p>The company is based in London, UK. Our projects often take place in other countries with work taking place accross Europe and beyond. We have a London based workshop for rack building and cable pre-fabrication.</p>
  </section>

  <section class="services">
    <h2 class="services-title">Services We Offer:</h2>
    <ul class="services-list">
      <li>Broadcast/AV system design</li>
      <li>On-site installation</li>
      <li>Rack building</li>
      <li>Pre-fabricated cable looms</li>
      <li>Fibre optic installation</li>
    </ul>
  </section>

  <div class="gallery">
    <div class="photo photo-cabling" role="img" aria-label="Photo of neatly wired control modules and cabling inside an equipment cabinet"></div>
    <div class="photo photo-rack" role="img" aria-label="Photo of an installed equipment rack with patch panels in a plant room"></div>
    <div class="photo photo-room" role="img" aria-label="Photo of a luxury living room with a wall-mounted television and sofas"></div>
  </div>

  <svg class="foreground" viewBox="0 0 846 1200" aria-hidden="true">
    <path d="M0 789 H120 C60 789 20 800 0 826 Z" fill="var(--paper)"/>
    <path d="M846 850 C800 960 760 1080 660 1099 H0 V1200 H846 Z" fill="var(--slate-blue)"/>
  </svg>

  <p class="web-address">www.<span>velcor-lane</span><b>.com</b></p>
</main>
</body>
</html>
```